Manufacturing company needs new business card.

I need a unique Business Card that will truly stand out. Nothing too busy. Simple is good, right? Not looking for a standard design either. No cookie cutter layout. I am just looking for something interesting and a bit different. Does't have to completely off the wall crazy, just not your run of the mill business card. Clean and modern with a touch of industrial.

Target Market(s)

Air conditioning industry, Architects, builders.

Industry/Entity Type

Business

Contact Information for Business Card

Details to be included on card are:

Peter Vance
Managing Director

T: 1300 847 519
M: 0428 593 174
W: www.brenvaleworks.com.au
E: peter.vance@brenvaleworks.com.au
A: 58 Harwick Lane, Sydney NSW 2000

Font styles to use
Sans Serif

Colors
0355a3
848484
fbfbfb

Requirements
Must have
• Card design must be landscape.

```html
<!DOCTYPE html>
<html lang="en">
<head>
<meta charset="utf-8">
<title>Brenvale Works – Business Card</title>
<link href="https://fonts.googleapis.com/css2?family=Lato:wght@300;400;700&display=swap" rel="stylesheet">
<style>
  :root {
    --brand-blue: #0b57a6;
    --text-blue: #1f5cae;
    --steel-grey: #7d7e7e;
    --light-grey: #ececec;
    --paper: #ffffff;
    --backdrop: #e4e4e4;
  }
  html, body {
    margin: 0;
    padding: 0;
    width: 1200px;
    height: 900px;
    overflow: hidden;
    background: var(--backdrop);
    font-family: "Lato", Arial, sans-serif;
  }
  .card {
    position: absolute;
    left: 310px;
    width: 580px;
    height: 340px;
    background: var(--paper);
    overflow: hidden;
  }
  .card--front { top: 70px; }
  .card--back  { top: 490px; }
  .card__shapes {
    position: absolute;
    inset: 0;
    width: 580px;
    height: 340px;
  }
  .brand {
    position: absolute;
    display: flex;
    align-items: center;
    gap: 8px;
    color: var(--text-blue);
    font-weight: 700;
    white-space: nowrap;
  }
  .brand__square {
    background: var(--brand-blue);
    display: block;
  }
  .brand--small { right: 20px; font-size: 17px; }
  .brand--small .brand__square { width: 20px; height: 20px; }
  .card--front .brand--small { top: 34px; }
  .card--back .brand--small { top: 22px; }
  .brand--large { left: 120px; top: 122px; font-size: 40px; gap: 16px; }
  .brand--large .brand__square { width: 44px; height: 44px; }

  .holder { position: absolute; left: 37px; top: 90px; color: var(--text-blue); }
  .holder__name { font-size: 27px; font-weight: 400; margin: 0; line-height: 1.1; }
  .holder__role { font-size: 13px; margin: 2px 0 0 30px; }

  .phones {
    position: absolute;
    right: 392px;
    top: 174px;
    text-align: right;
    color: var(--text-blue);
    font-size: 13.5px;
    font-weight: 300;
    line-height: 27px;
  }
  .details {
    position: absolute;
    left: 316px;
    top: 194px;
    color: var(--paper);
    font-size: 13px;
    font-weight: 300;
  }
  .details__row {
    display: flex;
    align-items: center;
    gap: 12px;
    height: 32px;
  }
  .details__row svg { width: 14px; height: 14px; flex: none; }
  .website {
    position: absolute;
    left: 0;
    right: 0;
    top: 296px;
    height: 44px;
    line-height: 44px;
    text-align: center;
    color: var(--paper);
    font-size: 13px;
    font-weight: 300;
  }
</style>
</head>
<body>

<section class="card card--front" aria-label="Business card front">
  <svg class="card__shapes" viewBox="0 0 580 340" aria-hidden="true">
    <rect x="0" y="0" width="580" height="14" fill="var(--steel-grey)"/>
    <rect x="446" y="14" width="134" height="118" fill="var(--light-grey)"/>
    <polygon points="0,14 196,14 170,76 0,76" fill="var(--brand-blue)"/>
    <polygon points="0,76 170,76 196,14 204,14 174,82 0,82" fill="var(--steel-grey)"/>
    <polygon points="312,132 580,132 580,137 316,137 280,282 274,282" fill="var(--steel-grey)"/>
    <polygon points="316,137 580,137 580,282 280,282" fill="var(--brand-blue)"/>
    <rect x="0" y="282" width="580" height="14" fill="var(--steel-grey)"/>
    <rect x="0" y="296" width="580" height="44" fill="var(--brand-blue)"/>
  </svg>

  <div class="brand brand--small"><span class="brand__square"></span>Brenvale Works</div>

  <div class="holder">
    <h1 class="holder__name">Peter Vance</h1>
    <p class="holder__role">Managing Director</p>
  </div>

  <div class="phones">
    <div>Mobile : 0428-593-174</div>
    <div>Tele : 1300-847-519</div>
  </div>

  <div class="details">
    <div class="details__row">
      <svg viewBox="0 0 14 14"><rect x="1" y="3" width="12" height="8" fill="#fff"/><polyline points="1,3 7,8 13,3" fill="none" stroke="var(--brand-blue)" stroke-width="1"/></svg>
      <span>peter.vance@brenvaleworks.com.au</span>
    </div>
    <div class="details__row">
      <svg viewBox="0 0 14 14"><path d="M7 0.5a4.5 4.5 0 0 1 4.5 4.5c0 3.2-4.5 8.5-4.5 8.5S2.5 8.2 2.5 5A4.5 4.5 0 0 1 7 0.5z" fill="#fff"/><circle cx="7" cy="5" r="1.7" fill="var(--brand-blue)"/></svg>
      <span>58 Harwick Lane, Sydney NSW 2000</span>
    </div>
  </div>

  <div class="website">www.brenvaleworks.com.au</div>
</section>

<section class="card card--back" aria-label="Business card back">
  <svg class="card__shapes" viewBox="0 0 580 340" aria-hidden="true">
    <polygon points="0,32 180,32 160,92 0,92" fill="var(--brand-blue)"/>
    <polygon points="0,92 160,92 180,32 188,32 166,98 0,98" fill="var(--steel-grey)"/>
    <polygon points="340,222 580,196 580,246 326,258 322,286 310,286" fill="var(--steel-grey)"/>
    <polygon points="326,258 580,246 580,280 322,286" fill="var(--brand-blue)"/>
    <rect x="0" y="296" width="580" height="44" fill="var(--brand-blue)"/>
  </svg>

  <div class="brand brand--small"><span class="brand__square"></span>Brenvale Works</div>
  <div class="brand brand--large"><span class="brand__square"></span>Brenvale Works</div>
</section>

</body>
</html>
```